Pale Ridge Wine Labels

Pale Ridge is an ultra-premium, allocation-only Napa Valley wine brand being built with one objective: to become a long-term cult collectible.

This is not a retail wine.
This is not a lifestyle brand.
This is not driven by marketing trends.

Production is intentionally limited. Access is controlled through private membership. Every decision—from vineyard sourcing to packaging—is made with long-term brand equity in mind.
We are looking for a label system that reflects that level of discipline.

Design a cult-level wine label system for Pale Ridge that communicates rarity, restraint, and authority at a glance.

This is not decorative Napa.
This must feel like it belongs next to Lanternfield, Dorsett, Quillbrook—and still stand apart.
Brand Positioning
Ultra-premium, allocation-only Napa wine
Private membership model (not retail-driven)
Production capped intentionally (scarcity is real, not marketing)
Designed to become a long-term collectible

Tone:

Controlled
Intentional
Confident
Understated power

If it feels “designed” or “trying”—it’s wrong.

Core Product Structure

You are designing a system, not a single label.

Foundation Wines:

Cabernet Sauvignon (primary SKU)
Signature Blend

Extensions (future / limited):

Limited Edition Blend (art-driven)
Reserve (ultra minimal, elevated version)
Creative Direction (Critical)

We are pursuing cult minimalism with tension.

Think:

Silence > noise
Precision > decoration
Material > graphics

This should feel:

Like it was inevitable, not created
Recognizable from across the room
Memorable after one exposure
Design Constraints

These are non-negotiable:

Bottle: Vetrelle Ostana (tall, powerful silhouette)
Glass: Deep antique green (near black)
Capsule: Matte black (baseline)
Front must work with:
Direct glass etching (ghost etch) OR
Minimal premium paper label

No loud colors.
No trendy typography.
No illustrative storytelling.

Brand Elements to Use
Primary mark: VII (Roman numeral 9)
Brand name: PALE RIDGE
Vintage (subtle, not dominant)

Optional concept element:

Varietal composition expressed as a refined system (e.g., “85 · 15” or structured numeric expression)
Design Goals

Your design should achieve:

Instant Recognition
Must be identifiable from 10 feet away
Tactile Value
Feels expensive before you touch it
Even better once you do
Aging Power
This must still look relevant in 20 years
System Cohesion
Cabernet and Blend must feel like a family
Not two separate brands
What We Are NOT Looking For

Avoid immediately:

Gold foil overload
Script fonts / calligraphy
Illustrated vineyards / animals / crests
Trendy “modern winery” aesthetics
Busy compositions
Obvious luxury clichés

If it looks like:

A Napa tasting room brand → reject
A startup wine brand → reject
Something you'd see on a grocery shelf → reject
Creative Territories to Explore

Designers should explore distinct directions, not minor variations:

Pure Etch Minimalism
VII only
Extremely subtle, almost invisible
Power through absence
Architectural Typography
Strong, controlled use of PALE RIDGE
Spatial tension, alignment-driven
Symbol + System
VII + numeric composition (85 / 15, etc.)
Feels like a formula, not decoration
Material-Driven Label
Paper, emboss, deboss, letterpress
Texture carries the design

Target Market(s)

Ultra-high-net-worth individuals, collectors, and allocation-driven wine buyers. Men and women 35–65 Entrepreneurs, executives, investors Already purchasing cult Napa wines ($250–$1,000+ per bottle) Psychographics: Value scarcity over availability Prefer private access over retail Buy for status, cellar, and long-term collection Appreciate restraint, not flash If it appeals to mass retail, it’s wrong.

Industry/Entity Type

Luxury Wine / Fine Wine / Ultra-Premium Consumer Goods

Requirements
Must have
• 1. Lanternfield Why it matters: True cult positioning Feels rare, quiet, and collector-driven What to take: Effortless authority Doesn’t try to look expensive—it just is Strong identity without noise What to avoid: Do not replicate illustration or vintage storytelling style 2. Quillbrook (Dorsett Family) Why it matters: Masterclass in restraint and architectural design What to take: Minimalism with structure Precision typography and spacing Confidence through reduction What to avoid: Don’t make it cold or overly corporate 3. Dorsett Estate Why it matters: One of the most iconic luxury wine labels ever What to take: Timelessness Balance of tradition + authority Label presence without excess What to avoid: Avoid classic/heritage clichés (crests, shields, etc.) 4. Tacet Duo Why it matters: Instantly recognizable globally Clean, iconic silhouette and branding system What to take: Immediate recognition from distance Cohesive system across vintages What to avoid: Don’t go mainstream or overly commercial 5. Hollow Falcon Why it matters: Pure scarcity-driven brand power What to take: Understated exclusivity Nothing feels added for effect What to avoid: Do not introduce illustration or narrative-driven visuals

```html
<!DOCTYPE html>
<html lang="en">
<head>
<meta charset="utf-8">
<title>Pale Ridge — Label Specification</title>
<link rel="stylesheet" href="https://fonts.googleapis.com/css2?family=Cinzel:wght@400&family=Cormorant+Garamond:ital,wght@1,500&family=Playfair+Display:wght@400&display=swap">
<style>
  :root {
    --backdrop: #a9a9a9;
    --label-paper: #ffffff;
    --ink: #0d0d0d;
    --pointer: #7b7b7b;
  }
  html, body {
    margin: 0;
    padding: 0;
    width: 1200px;
    height: 1200px;
    overflow: hidden;
    background: var(--backdrop);
  }
  .spec-sheet {
    display: block;
    width: 1200px;
    height: 1200px;
  }
  .label-paper { fill: var(--label-paper); }
  .brand-mark,
  .brand-name {
    font-family: "Cinzel", serif;
    font-weight: 400;
    fill: var(--ink);
  }
  .blend-ratio {
    font-family: "Playfair Display", serif;
    font-weight: 400;
    fill: var(--ink);
  }
  .callout-note {
    font-family: "Cormorant Garamond", serif;
    font-style: italic;
    font-weight: 500;
    font-size: 48px;
    fill: var(--ink);
  }
  .callout-pointer {
    stroke: var(--pointer);
    stroke-width: 7;
    fill: none;
  }
  .callout-head { fill: var(--pointer); }
</style>
</head>
<body>
<svg class="spec-sheet" viewBox="0 0 1200 1200" xmlns="http://www.w3.org/2000/svg">
  <defs>
    <marker id="pointer-head" viewBox="0 0 10 10" refX="8" refY="5" markerWidth="30" markerHeight="30" markerUnits="userSpaceOnUse" orient="auto">
      <path class="callout-head" d="M0,0 L10,5 L0,10 Z"/>
    </marker>
  </defs>

  <g class="spec-layout" transform="translate(231 30) scale(0.625)">
    <!-- Front label -->
    <g class="front-label">
      <rect class="label-paper" x="162" y="462" width="858" height="1008" role="img" aria-label="Textured paper label with torn edges and crossing grey diagonal bands"/>
      <text class="brand-mark" x="590" y="910" text-anchor="middle" font-size="240">VII</text>
      <text class="brand-name" x="590" y="1068" text-anchor="middle" font-size="84" textLength="720" lengthAdjust="spacingAndGlyphs">PALE RIDGE</text>
      <text class="blend-ratio" x="591" y="1272" text-anchor="middle" font-size="64">85 · 15</text>
    </g>

    <!-- Finish callouts -->
    <g class="callouts">
      <text class="callout-note" x="287" y="350">white embossed text</text>
      <line class="callout-pointer" x1="545" y1="632" x2="410" y2="383" marker-end="url(#pointer-head)"/>

      <text class="callout-note" x="815" y="288">embossed texture.</text>
      <line class="callout-pointer" x1="828" y1="578" x2="958" y2="324" marker-end="url(#pointer-head)"/>

      <text class="callout-note" x="783" y="736">embossed text</text>
      <text class="callout-note" x="783" y="793">gold foil</text>
      <line class="callout-pointer" x1="714" y1="995" x2="842" y2="810" marker-end="url(#pointer-head)"/>

      <line class="callout-pointer" x1="520" y1="1323" x2="390" y2="1493" marker-end="url(#pointer-head)"/>
      <text class="callout-note" x="180" y="1568">white embossed text</text>
    </g>
  </g>
</svg>
</body>
</html>
```